WordPress Design for both website and landing page for an expert

I need a clean and stylish design for my new website. I work as an expert (see attached file WHY HOW WHAT), my product is expert opinion (reports) for company evaluations You can use all of the attached pictures colored or black / white. The person is me, you can add other pictures, if you want. The design should be clean and stylish, so you could use white, black, gray, silver and / or one additional color. I have added an idea about my website, see attached file CONCEPT WEBSITE If you have any more information, please do not hesitate to contact us 'Hesitate to ask me ...

```html
<!DOCTYPE html>
<html lang="en">
<head>
<meta charset="utf-8">
<title>Contact – Lukas Brenner</title>
<link href="https://fonts.googleapis.com/css2?family=Montserrat:wght@400;500;600&display=swap" rel="stylesheet">
<style>
  :root {
    --ink: #1f2328;
    --muted: #7d848c;
    --muted-light: #a3a9b0;
    --accent-nav: #9aa6a6;
    --field: #eef2f5;
    --map-light: #cdd0d3;
    --map-dark: #b4b8bc;
    --sky-top: #1f5fa8;
    --sky-mid: #4f86c0;
    --water: #1b3f66;
    --footer: #383d45;
    --footer-text: #a8adb4;
    --white: #ffffff;
  }
  * { box-sizing: border-box; margin: 0; padding: 0; }
  html, body { width: 1080px; height: 1200px; overflow: hidden; background: var(--white); }
  body { position: relative; font-family: 'Montserrat', sans-serif; color: var(--ink); }

  .brand {
    position: absolute; left: 43px; top: 30px; width: 200px;
    text-align: center; font-size: 17px; font-weight: 400; letter-spacing: 2.5px;
    color: var(--ink); text-transform: uppercase; white-space: nowrap;
  }
  .brand-mark { display: block; width: 30px; height: 30px; margin: 0 auto 12px; background: var(--ink); }

  .main-nav { position: absolute; top: 53px; left: 533px; right: 63px; display: flex; justify-content: space-between; }
  .main-nav a {
    font-size: 11.5px; font-weight: 500; letter-spacing: 2px; text-transform: uppercase;
    color: var(--ink); text-decoration: none;
  }
  .main-nav a.is-current { color: var(--accent-nav); }

  .hero { position: absolute; left: 123px; top: 177px; width: 833px; height: 339px; display: flex; }
  .hero-photo {
    width: 417px; height: 100%;
    background: linear-gradient(180deg, var(--sky-top) 0%, var(--sky-mid) 45%, #6f88a8 55%, var(--water) 80%, #14273f 100%);
  }
  .hero-map { flex: 1; height: 100%; background: linear-gradient(90deg, var(--map-dark) 0%, var(--map-light) 45%, #dcdedf 100%); }
  .hero-title {
    position: absolute; left: 310px; top: 122px; width: 210px;
    text-align: center; color: var(--white); font-size: 38px; font-weight: 500;
    letter-spacing: 2px; line-height: 42px; text-transform: uppercase;
    text-shadow: 0 1px 8px rgba(30, 35, 40, 0.35);
  }

  .contact-points { position: absolute; top: 592px; left: 0; width: 1080px; }
  .contact-point { position: absolute; width: 260px; text-align: center; }
  .contact-point svg { display: block; margin: 0 auto; }
  .contact-value { font-size: 15px; color: var(--muted); letter-spacing: 0.3px; }
  .contact-note { font-size: 10.5px; color: var(--muted); margin-top: 6px; }
  .contact-address { font-size: 11.5px; color: var(--muted); line-height: 19px; letter-spacing: 0.4px; }
  .point-phone { left: 209px; }
  .point-address { left: 409px; }
  .point-mail { left: 610px; }

  .help-heading {
    position: absolute; top: 738px; left: 0; width: 1080px; text-align: center;
    font-size: 24px; font-weight: 500; line-height: 30px; color: var(--ink);
  }

  .contact-form { position: absolute; left: 255px; top: 833px; width: 570px; }
  .field {
    position: absolute; height: 35px; background: var(--field); border-radius: 2px;
    font-size: 9.5px; letter-spacing: 1.2px; color: var(--muted-light); text-transform: uppercase;
    padding: 13px 0 0 19px;
  }
  .field-name { left: 0; width: 200px; }
  .field-email { left: 216px; width: 200px; }
  .field-phone { left: 432px; width: 138px; }
  .field-message { top: 53px; left: 0; width: 570px; height: 114px; padding-top: 12px; }
  .submit-button {
    position: absolute; top: 207px; left: 219px; width: 131px; height: 36px;
    border: 1.5px solid #c4c8cc; border-radius: 18px; background: var(--white);
    font-family: 'Montserrat', sans-serif; font-size: 11.5px; font-weight: 600;
    letter-spacing: 1.5px; color: var(--ink);
  }

  .site-footer { position: absolute; left: 0; top: 1138px; width: 1080px; height: 62px; background: var(--footer); }
  .copyright { position: absolute; left: 123px; top: 25px; font-size: 10px; color: var(--footer-text); letter-spacing: 0.3px; }
  .legal-links { position: absolute; right: 123px; top: 25px; font-size: 10px; color: var(--footer-text); letter-spacing: 0.3px; }
  .legal-links span { margin: 0 8px; }
  .to-top {
    position: absolute; left: 999px; top: 12px; width: 38px; height: 38px; border-radius: 50%;
    background: #8b9097; display: flex; align-items: center; justify-content: center;
  }
</style>
</head>
<body>
  <header>
    <div class="brand"><span class="brand-mark"></span>Lukas Brenner</div>
    <nav class="main-nav">
      <a href="#">Home</a>
      <a href="#">About</a>
      <a href="#">What I do</a>
      <a href="#">Why / How I do</a>
      <a href="#" class="is-current">Contact</a>
    </nav>
  </header>

  <section class="hero">
    <div class="hero-photo" role="img" aria-label="Evening city skyline with a tall TV tower and a river harbour"></div>
    <div class="hero-map" role="img" aria-label="Grey road map of Germany and neighbouring countries"></div>
    <h1 class="hero-title">Contact me</h1>
  </section>

  <section class="contact-points">
    <div class="contact-point point-phone">
      <svg width="22" height="22" viewBox="0 0 24 24" fill="none" stroke="#555b62" stroke-width="1.3" stroke-linejoin="round">
        <path d="M6.5 3.5l3 3.2-1.8 2.2c1 2.3 3 4.3 5.4 5.4l2.2-1.8 3.2 3-1.9 2.9C10.8 18.6 5.4 13.2 3.6 5.4z"/>
      </svg>
      <p class="contact-value" style="margin-top:15px">+1-303-555-0148</p>
      <p class="contact-note">Call Us Today!</p>
    </div>
    <div class="contact-point point-address">
      <svg width="22" height="28" viewBox="0 0 22 28" fill="none" stroke="#555b62" stroke-width="1.4">
        <path d="M11 26C5 18 2.5 13.5 2.5 10a8.5 8.5 0 0 1 17 0c0 3.5-2.5 8-8.5 16z"/>
        <circle cx="11" cy="10" r="2.6"/>
      </svg>
      <p class="contact-address" style="margin-top:11px">48 Linden Terrace<br>Fairview, OH 44126<br>Germany</p>
    </div>
    <div class="contact-point point-mail">
      <svg width="24" height="22" viewBox="0 0 24 22" fill="none" stroke="#555b62" stroke-width="1.4">
        <rect x="2" y="5" width="20" height="13"/>
        <path d="M2 5l10 8 10-8"/>
      </svg>
      <p class="contact-value" style="margin-top:15px">hello@brenner-mail.com</p>
      <p class="contact-note">Inquire Now!</p>
    </div>
  </section>

  <h2 class="help-heading">How can I help<br>you today!</h2>

  <form class="contact-form">
    <div class="field field-name">Enter your name</div>
    <div class="field field-email">Email</div>
    <div class="field field-phone">Phone</div>
    <div class="field field-message">Message</div>
    <button type="button" class="submit-button">SUBMIT</button>
  </form>

  <footer class="site-footer">
    <p class="copyright">© 2018 Lukas M. Brenner. All Rights Reserved</p>
    <p class="legal-links">Data protection<span>I</span>Cookies<span>I</span>imprint</p>
    <div class="to-top">
      <svg width="10" height="12" viewBox="0 0 10 12" fill="none" stroke="#ffffff" stroke-width="1.2">
        <path d="M5 11V1M2 4l3-3 3 3"/>
      </svg>
    </div>
  </footer>
</body>
</html>
```